Card Design Project

We are looking for a couple card / box designs that will for a new company that is in the bereavement assistance industry.
Our customers are churches, counseling centers and funeral homes.
Once we have these card designs we will need to work with that same artist to help us out with box graphic designs that are similar to the card designs. The box is 12" long x 4" wide x 6" high
We will need more designs in the future so we are looking for an artist for future work.
Our look needs to be professional and solemn.
The front of the card should be quite close to what i am attaching but with some professional touches to it that give it a proper look. We dont want you to stray to far from what i have attached but if you feel you have some good ideas we would be more than happy to see them.
The back of the card we want people to be able to leave the family a note so will need wording such as "leave a message to the family" or "write a memory"
Keep in mind we will need this look to be able to match graphics on the box as well, we kind of need the card design and box design to go together.
Thanks
Just wanted to mention to all designers that although we would like our logo on the card it is something that we need to keep kind of in the background somehow. We cant be seen as trying to push a brand name too much so please keep that in mind. Thanks
Reason: HOLIDAY
Designers, I took the need to see what the design looked like on a box out.
Reason: just need a bit of extra time guys, thanks for all who are helping us on this!
Target Market(s)
Funeral homes, churches, counseling centers
Industry/Entity Type
Industry
Requirements
Must have
- Professional and solemn look
Card need to be 4"wide X 6" high and needs to be portrait
A pin will be attached to the top right part of the card so will need a space there for it.
I was thinking that we would have the pic of the ribbon symbol there so when the pin is off the card there would still be a ribbon pic there. The pins that we will be attaching are ribbon pins similar to what i have on my pdf's
Please keep in mind that we cant really have out logo in a dominant area on the card. We would like to have it subtly in there but not to where it is in your face type of thing.
Nice to have
- Our logo but very small, not to intrusive .
Would like 2 designs, one dark and another light.
Maybe 1 masculine or gender neutral and another feminine
Wording should be the same

```html
<!DOCTYPE html>
<html lang="en">
<head>
<meta charset="utf-8">
<title>Dear Friends – Memorial Card</title>
<link rel="stylesheet" href="https://fonts.googleapis.com/css2?family=Cormorant+Garamond:ital,wght@1,500;1,600&display=swap">
<style>
  :root {
    --paper: #ffffff;
    --ink: #111111;
    --frame: #1a1a1a;
    --rule: #8a8a8a;
    --ribbon-dark: #2b2b2b;
    --ribbon-light: #6a6a6a;
    --feather-mid: #bdbdbd;
    --feather-light: #f2f2f2;
  }
  * { box-sizing: border-box; margin: 0; padding: 0; }
  html, body {
    width: 1200px;
    height: 848px;
    overflow: hidden;
    background: var(--paper);
  }
  .sheet {
    position: relative;
    width: 1200px;
    height: 848px;
    font-family: "Cormorant Garamond", "Times New Roman", serif;
    font-style: italic;
    color: var(--ink);
  }
  .card {
    position: absolute;
    background: var(--paper);
  }
  .card--front {
    left: 15px; top: 13px;
    width: 542px; height: 813px;
    border: 1px solid var(--frame);
  }
  .card--back {
    left: 640px; top: 11px;
    width: 544px; height: 815px;
    border: 2px solid var(--frame);
  }
  .greeting {
    position: absolute;
    left: 160px; top: 88px;
    font-size: 40px;
    font-weight: 500;
    line-height: 1;
  }
  .ribbon {
    position: absolute;
    left: 390px; top: 31px;
    width: 113px; height: 122px;
  }
  .feather {
    position: absolute;
    left: 54px; top: 490px;
    width: 428px; height: 320px;
    background: radial-gradient(ellipse 60% 28% at 45% 32%, var(--feather-mid), var(--feather-light) 70%, transparent 100%),
                linear-gradient(to bottom, transparent 55%, rgba(230,230,230,0.6) 70%, transparent 100%);
  }
  .message {
    position: absolute;
    left: 0; top: 204px;
    width: 100%;
    text-align: center;
    font-size: 19px;
    font-weight: 500;
    line-height: 34px;
  }
  .message p { margin-bottom: 34px; }
  .closing {
    position: absolute;
    left: 0; top: 679px;
    width: 100%;
    text-align: center;
    font-size: 19px;
    font-weight: 600;
    line-height: 34px;
  }
  .memory-label {
    position: absolute;
    left: 50px; top: 361px;
    font-size: 25px;
    font-weight: 500;
    line-height: 34px;
  }
  .memory-lines {
    position: absolute;
    left: 250px; top: 34px;
    width: 262px; height: 736px;
    background: repeating-linear-gradient(to bottom, transparent 0 31px, var(--rule) 31px 32px);
  }
</style>
</head>
<body>
<main class="sheet">
  <section class="card card--front">
    <h1 class="greeting">Dear Friends</h1>
    <svg class="ribbon" viewBox="0 0 113 122" role="img" aria-label="Dark grey awareness ribbon emblem">
      <defs>
        <linearGradient id="ribbonTone" x1="0" y1="0" x2="1" y2="1">
          <stop offset="0" stop-color="var(--ribbon-light)"/>
          <stop offset="1" stop-color="var(--ribbon-dark)"/>
        </linearGradient>
      </defs>
      <rect width="113" height="122" rx="10" fill="url(#ribbonTone)"/>
    </svg>
    <div class="message">
      <p>Your support in attending this memorial<br>and celebration of life means so much to us.</p>
      <p>Our loved one has touched you in ways<br>we may not even recognize yet.</p>
      <p>We invite you to wear this pin through<br>your grieving process, which we receive as<br>a symbol of your sympathy and support &nbsp;of our loss.</p>
    </div>
    <div class="feather" role="img" aria-label="Soft white feather lying on a reflective surface"></div>
    <p class="closing">Thank you for grieving together with us</p>
  </section>

  <section class="card card--back">
    <h2 class="memory-label">Write a memory</h2>
    <div class="memory-lines" aria-hidden="true"></div>
  </section>
</main>
</body>
</html>
```